Ancient Art and Artifact information website

Hello Designers,
We are starting up a new website who talk abut and discusses an ancient arts artifacts. We would covering a wide range of countries ranging from Egypt, Greece, India, Syria, Rome, etc. My website name Tarn Wisp
Designs that fits with ancient theme and some kind of uniqueness would be accepted.
Requirements:
1) A home page design
2) Sub page design
3) A suitable logo
Sections can be added are featured ancient arts/places with short description followed by a more button, latest news, and comment section.
Add contents if you found relevant for this category of website. Ability to share the information through social media is desired.
Must be a responsive design. I look forward to designs which are mind blowing.
Number of Pages Required
2 page

```html
<!DOCTYPE html>
<html lang="en">
<head>
<meta charset="utf-8">
<title>Tarn Wisp — Ancient Arts</title>
<link rel="stylesheet" href="https://fonts.googleapis.com/css2?family=Roboto:wght@400;500;700&family=Montserrat:wght@600;700&display=swap">
<style>
:root{
  --gold:#d4a437;
  --gold-light:#e8c05a;
  --gold-dark:#9c7019;
  --orange:#f2a21c;
  --panel:#1c1c1c;
  --panel-2:#262626;
  --line:#3c3c3c;
  --band:#4b4b4b;
  --text:#7a7a7a;
  --text-light:#b9b9b9;
  --white:#f2f2f2;
  --black:#000;
}
*{box-sizing:border-box;margin:0;padding:0}
html,body{width:1200px;height:2308px;overflow:hidden}
body{
  font-family:"Roboto",Arial,sans-serif;
  background:
    radial-gradient(ellipse 700px 500px at 300px 300px,rgba(120,90,45,.35),transparent 70%),
    radial-gradient(ellipse 600px 500px at 1000px 150px,rgba(110,85,40,.3),transparent 70%),
    linear-gradient(180deg,#4b3a21 0,#3b2d18 380px,#2c2111 700px,#120d06 900px,#000 1000px,#000 1940px,#1c150c 2080px,#3e301c 2200px,#54432a 2308px);
  position:relative;color:var(--text);
}
.abs{position:absolute}

/* header */
.nav-bar{left:143px;top:65px;width:914px;height:61px;background:linear-gradient(#303030,#1f1f1f);border:1px solid #5a5a5a;box-shadow:0 4px 10px rgba(0,0,0,.6)}
.nav-bar::after{content:"";position:absolute;inset:6px;border:1px solid #4a4a4a}
.nav-link{top:86px;font-size:14px;color:var(--gold-light);text-decoration:none}
.nav-link.is-active{color:var(--orange)}
.nav-login{left:969px;top:84px;width:59px;height:22px;background:linear-gradient(var(--gold-light),var(--gold-dark));color:#2a1c04;font-size:13px;text-align:center;line-height:22px;border:1px solid #2a1c04}
.brand{left:528px;top:38px;width:144px;height:124px;background:#1b1b1b;border:2px solid #3a3a3a;display:flex;align-items:center;justify-content:center;text-align:center;box-shadow:0 6px 14px rgba(0,0,0,.7)}
.brand-name{font-family:"Roboto",sans-serif;font-weight:700;font-size:27px;line-height:28px;color:var(--gold);text-transform:uppercase}

/* featured */
.featured{left:143px;top:195px;width:914px;height:300px;background:var(--panel);border:2px solid #3e3e3e;box-shadow:0 6px 16px rgba(0,0,0,.6)}
.featured::after{content:"";position:absolute;inset:13px;border:1px solid #3b3b3b}
.featured-tab{left:455px;top:181px;width:291px;height:40px;background:#1e1e1e;border:2px solid #3e3e3e;border-top:none;clip-path:polygon(0 0,100% 0,94% 100%,6% 100%);color:var(--white);font-size:15px;letter-spacing:.3px;text-align:center;line-height:38px}
.featured-tab span{color:var(--gold)}
.featured-image{left:171px;top:249px;width:437px;height:209px;background:linear-gradient(135deg,#b88f4f,#d8b274 45%,#8a6232);box-shadow:0 4px 10px rgba(0,0,0,.7)}
.featured-caption{left:185px;top:437px;font-size:12px;color:#f0e0c0}
.featured-title{left:648px;top:257px;font-size:26px;color:var(--white)}
.featured-sub{left:648px;top:287px;font-size:14px;color:var(--gold);font-weight:500}
.featured-text{left:648px;top:322px;width:370px;font-size:11px;line-height:18.5px;color:#8a8a8a}
.btn{background:linear-gradient(var(--gold-light),var(--gold-dark));color:#241804;font-weight:700;text-align:center;text-transform:uppercase}
.featured-more{left:649px;top:429px;width:74px;height:26px;font-size:12px;line-height:26px}
.featured-corner{left:979px;top:415px;width:78px;height:80px;background:linear-gradient(135deg,var(--gold-light),var(--gold-dark));clip-path:polygon(100% 0,100% 100%,0 100%)}
.featured-corner svg{position:absolute;right:10px;bottom:10px}

/* ribbons */
.ribbon{height:62px}
.ribbon svg{position:absolute;inset:0;width:100%;height:100%}
.ribbon h2{position:absolute;left:0;right:0;top:4px;text-align:center;font-size:33px;font-weight:500;color:#fff6e0;line-height:46px;text-shadow:0 1px 2px rgba(60,40,0,.6)}

/* cards */
.card{top:635px;width:291px;height:292px;background:var(--panel);box-shadow:0 4px 10px rgba(0,0,0,.6)}
.card-image{height:151px}
.card-title{height:38px;background:var(--band);color:var(--white);font-size:18px;text-align:center;line-height:38px}
.card-text{padding:18px 22px 0;font-size:11px;line-height:19px;color:#6f6f6f}
.card-foot{position:absolute;left:22px;right:22px;bottom:15px;height:20px;display:flex;align-items:center;justify-content:space-between}
.btn-sm{width:52px;height:20px;font-size:10px;line-height:20px}
.stats{display:flex;gap:12px;font-size:10px;color:#7a7a7a;align-items:center}
.stats span{display:flex;align-items:center;gap:4px}
.arrow-btn{top:764px;width:28px;height:28px;background:linear-gradient(var(--gold),var(--gold-dark));display:flex;align-items:center;justify-content:center}

/* gallery */
.tile{overflow:hidden;box-shadow:0 4px 10px rgba(0,0,0,.7)}
.tile::after{content:"";position:absolute;inset:7px;border:1px solid rgba(212,164,55,.7)}
.tile-fill{position:absolute;inset:0}
.tile-cap{position:absolute;left:0;right:0;bottom:16px;text-align:center;z-index:1}
.tile-name{font-family:"Montserrat",sans-serif;font-weight:700;font-size:14px;color:#fff;text-shadow:0 1px 3px #000}
.tile-place{font-family:"Montserrat",sans-serif;font-weight:600;font-size:10px;color:var(--gold)}

/* news */
.news{width:447px;height:143px;background:var(--panel);box-shadow:0 4px 10px rgba(0,0,0,.6)}
.news-image{position:absolute;left:0;top:0;width:134px;height:143px}
.news-body{position:absolute;left:142px;top:8px;right:8px;bottom:8px;border:1px solid #3a3a3a;padding:17px 0 0 14px}
.news-title{font-size:13.5px;font-weight:500;color:var(--gold)}
.news-text{margin-top:8px;width:270px;font-size:11px;line-height:18px;color:#6f6f6f}
.news-foot{position:absolute;left:14px;right:12px;bottom:12px;display:flex;justify-content:space-between;align-items:center}
.more-news{left:544px;top:2102px;width:111px;height:27px;font-size:13px;line-height:27px}

/* footer */
.footer{left:0;top:2172px;width:1200px;height:86px;background:#1d1d1d}
.footer-brand{left:143px;top:2146px;width:149px;height:130px;background:#1b1b1b;border:2px solid #3a3a3a;display:flex;align-items:center;justify-content:center;text-align:center;box-shadow:0 6px 14px rgba(0,0,0,.7)}
.footer-nav{left:403px;top:2193px;display:flex;gap:10px;font-size:13px;color:var(--gold-light)}
.footer-nav .is-active{color:var(--orange)}
.copyright{left:494px;top:2224px;font-size:9px;color:#555;letter-spacing:.5px}
.social{top:2203px;width:24px;height:24px;border-radius:50%;background:#4a4a4a}
</style>
</head>
<body>

<!-- header -->
<div class="abs nav-bar"></div>
<a class="abs nav-link is-active" style="left:168px">Home</a>
<a class="abs nav-link" style="left:245px">Ancient Arts</a>
<a class="abs nav-link" style="left:368px">History</a>
<a class="abs nav-link" style="left:452px">News</a>
<a class="abs nav-link" style="left:705px">Gallery</a>
<a class="abs nav-link" style="left:792px">Articles</a>
<a class="abs nav-link" style="left:883px">Contact</a>
<div class="abs nav-login">Login</div>
<div class="abs brand"><div class="brand-name">Tarn<br>Wisp</div></div>

<!-- featured -->
<section class="abs featured"></section>
<div class="abs featured-tab"><span>• • • •</span> FEATURED ANCIENT ARTS <span>• • • •</span></div>
<div class="abs featured-image" role="img" aria-label="Carved stone relief of ancient figures"></div>
<div class="abs featured-caption">Ancient Art, Egypt</div>
<h1 class="abs featured-title" style="font-weight:400">Ancient Greek art</h1>
<div class="abs featured-sub">The standard Lorem Ipsum passage, used since the 1500s</div>
<p class="abs featured-text">Sed ut perspiciatis unde omnis iste natus error sit voluptatem accusantium doloremque laudantium, totam rem aperiam, eaque ipsa quae ab illo inventore veritatis et quasi architecto beatae vitae dicta sunt explicabo. Nemo enim ipsam voluptatem quia voluptas sit aspernatur aut odit aut fugit, sed quia.</p>
<div class="abs btn featured-more">More</div>
<div class="abs featured-corner">
  <svg width="36" height="14" viewBox="0 0 36 14"><path d="M9 2 4 7l5 5M27 2l5 5-5 5" fill="none" stroke="#2a1c04" stroke-width="2"/></svg>
</div>

<!-- popular -->
<div class="abs ribbon" style="left:351px;top:535px;width:498px">
  <svg viewBox="0 0 500 62" preserveAspectRatio="none">
    <polygon points="0,22 72,22 72,60 0,60 18,41" fill="#a8781c"/>
    <polygon points="500,22 428,22 428,60 500,60 482,41" fill="#a8781c"/>
    <polygon points="40,50 72,60 72,50" fill="#5e420c"/>
    <polygon points="460,50 428,60 428,50" fill="#5e420c"/>
    <rect x="40" y="2" width="420" height="48" fill="#c99a30"/>
    <rect x="40" y="2" width="420" height="48" fill="url(#gold)"/>
    <defs><linearGradient id="gold" x1="0" y1="0" x2="1" y2="1"><stop offset="0" stop-color="#e2b44a"/><stop offset=".5" stop-color="#c2912a"/><stop offset="1" stop-color="#9e7019"/></linearGradient></defs>
  </svg>
  <h2>Popular Ancient Arts</h2>
</div>

<div class="abs arrow-btn" style="left:91px"><svg width="10" height="12"><path d="M7 1 2 6l5 5" fill="none" stroke="#1a1204" stroke-width="2"/></svg></div>
<div class="abs arrow-btn" style="left:1081px"><svg width="10" height="12"><path d="M3 1l5 5-5 5" fill="none" stroke="#1a1204" stroke-width="2"/></svg></div>

<article class="abs card" style="left:141px">
  <div class="card-image" role="img" aria-label="Egyptian hieroglyph wall carving" style="background:linear-gradient(135deg,#c99a50,#8a5e24)"></div>
  <div class="card-title">Egypt</div>
  <p class="card-text">Sed ut perspiciatis unde omnis iste natus error sit voluptatem edusa accusant.</p>
  <div class="card-foot"><div class="btn btn-sm">More</div><div class="stats"><span><svg width="10" height="9" viewBox="0 0 10 9"><path d="M5 9 1 5A2.3 2.3 0 0 1 5 1.6 2.3 2.3 0 0 1 9 5Z" fill="#7a7a7a"/></svg>457</span><span><svg width="11" height="9" viewBox="0 0 11 9"><path d="M0 0h11v6H4L1 9V6H0Z" fill="#7a7a7a"/></svg>65</span></div></div>
</article>
<article class="abs card" style="left:455px">
  <div class="card-image" role="img" aria-label="Greek temple ruins under a blue sky" style="background:linear-gradient(180deg,#5a6f95,#9aa8be 50%,#6d6552)"></div>
  <div class="card-title">Greece</div>
  <p class="card-text">Sed ut perspiciatis unde omnis iste natus error sit voluptatem edusa accusant.</p>
  <div class="card-foot"><div class="btn btn-sm">More</div><div class="stats"><span><svg width="10" height="9" viewBox="0 0 10 9"><path d="M5 9 1 5A2.3 2.3 0 0 1 5 1.6 2.3 2.3 0 0 1 9 5Z" fill="#7a7a7a"/></svg>457</span><span><svg width="11" height="9" viewBox="0 0 11 9"><path d="M0 0h11v6H4L1 9V6H0Z" fill="#7a7a7a"/></svg>65</span></div></div>
</article>
<article class="abs card" style="left:767px">
  <div class="card-image" role="img" aria-label="Carved Indian temple pillars" style="background:linear-gradient(135deg,#a4643a,#6e3b1e)"></div>
  <div class="card-title">India</div>
  <p class="card-text">Sed ut perspiciatis unde omnis iste natus error sit voluptatem edusa accusant.</p>
  <div class="card-foot"><div class="btn btn-sm">More</div><div class="stats"><span><svg width="10" height="9" viewBox="0 0 10 9"><path d="M5 9 1 5A2.3 2.3 0 0 1 5 1.6 2.3 2.3 0 0 1 9 5Z" fill="#7a7a7a"/></svg>457</span><span><svg width="11" height="9" viewBox="0 0 11 9"><path d="M0 0h11v6H4L1 9V6H0Z" fill="#7a7a7a"/></svg>65</span></div></div>
</article>

<!-- gallery -->
<div class="abs ribbon" style="left:425px;top:966px;width:349px">
  <svg viewBox="0 0 500 62" preserveAspectRatio="none">
    <polygon points="0,22 100,22 100,60 0,60 24,41" fill="#a8781c"/>
    <polygon points="500,22 400,22 400,60 500,60 476,41" fill="#a8781c"/>
    <polygon points="58,50 100,60 100,50" fill="#5e420c"/>
    <polygon points="442,50 400,60 400,50" fill="#5e420c"/>
    <rect x="58" y="2" width="384" height="48" fill="url(#gold)"/>
  </svg>
  <h2>Gallery</h2>
</div>

<figure class="abs tile" style="left:141px;top:1070px;width:220px;height:407px">
  <div class="tile-fill" role="img" aria-label="Roman battle relief carved in stone" style="background:linear-gradient(160deg,#8c8a86,#55524d 60%,#3a3835)"></div>
  <figcaption class="tile-cap"><div class="tile-name">Roman Art</div><div class="tile-place">Italy</div></figcaption>
</figure>
<figure class="abs tile" style="left:377px;top:1070px;width:215px;height:193px">
  <div class="tile-fill" role="img" aria-label="Stone chariot at Hampi temple" style="background:linear-gradient(170deg,#a48464,#6e5236)"></div>
  <figcaption class="tile-cap"><div class="tile-name">Hampi Temple</div><div class="tile-place">India</div></figcaption>
</figure>
<figure class="abs tile" style="left:607px;top:1070px;width:216px;height:193px">
  <div class="tile-fill" role="img" aria-label="Painted Egyptian temple relief" style="background:linear-gradient(150deg,#c08a4c,#7c4a22)"></div>
  <figcaption class="tile-cap"><div class="tile-name">Temple Art</div><div class="tile-place">Egypt</div></figcaption>
</figure>
<figure class="abs tile" style="left:838px;top:1070px;width:219px;height:407px">
  <div class="tile-fill" role="img" aria-label="Carved stone Buddha statue" style="background:linear-gradient(160deg,#7a5442,#4a2e22 60%,#2e1c14)"></div>
  <figcaption class="tile-cap"><div class="tile-name">Budha Statue</div><div class="tile-place">China</div></figcaption>
</figure>
<figure class="abs tile" style="left:377px;top:1281px;width:215px;height:196px">
  <div class="tile-fill" role="img" aria-label="Columns of the Karnak temple" style="background:linear-gradient(180deg,#5d7fb0,#b48a5c 45%,#7a5632)"></div>
  <figcaption class="tile-cap"><div class="tile-name">Temples of Karnak</div><div class="tile-place">Egypt</div></figcaption>
</figure>
<figure class="abs tile" style="left:607px;top:1281px;width:216px;height:196px">
  <div class="tile-fill" role="img" aria-label="Ruined arches of Palmyra" style="background:linear-gradient(180deg,#6f8fbe,#c8a474 50%,#9a7446)"></div>
  <figcaption class="tile-cap"><div class="tile-name">Palmyra City</div><div class="tile-place">Syria</div></figcaption>
</figure>

<!-- news -->
<div class="abs ribbon" style="left:425px;top:1510px;width:349px">
  <svg viewBox="0 0 500 62" preserveAspectRatio="none">
    <polygon points="0,22 100,22 100,60 0,60 24,41" fill="#a8781c"/>
    <polygon points="500,22 400,22 400,60 500,60 476,41" fill="#a8781c"/>
    <polygon points="58,50 100,60 100,50" fill="#5e420c"/>
    <polygon points="442,50 400,60 400,50" fill="#5e420c"/>
    <rect x="58" y="2" width="384" height="48" fill="url(#gold)"/>
  </svg>
  <h2>Latest News</h2>
</div>

<article class="abs news" style="left:141px;top:1610px">
  <div class="news-image" role="img" aria-label="Antique brass instruments" style="background:linear-gradient(135deg,#9c6a38,#4e2e18)"></div>
  <div class="news-body"><h3 class="news-title">The standard Lorem Ipsum passage</h3><p class="news-text">Sed ut perspiciatis unde omnis iste natus error sit voluptatem edusa accusant enim ipsam.</p>
  <div class="news-foot"><div class="stats"><span><svg width="10" height="9" viewBox="0 0 10 9"><path d="M5 9 1 5A2.3 2.3 0 0 1 5 1.6 2.3 2.3 0 0 1 9 5Z" fill="#7a7a7a"/></svg>457</span><span><svg width="11" height="9" viewBox="0 0 11 9"><path d="M0 0h11v6H4L1 9V6H0Z" fill="#7a7a7a"/></svg>65</span></div><div class="btn btn-sm">More</div></div></div>
</article>
<article class="abs news" style="left:611px;top:1610px">
  <div class="news-image" role="img" aria-label="Rows of terracotta warrior statues" style="background:linear-gradient(135deg,#a09a92,#5a544c)"></div>
  <div class="news-body"><h3 class="news-title">The standard Lorem Ipsum passage</h3><p class="news-text">Sed ut perspiciatis unde omnis iste natus error sit voluptatem edusa accusant enim ipsam.</p>
  <div class="news-foot"><div class="stats"><span><svg width="10" height="9" viewBox="0 0 10 9"><path d="M5 9 1 5A2.3 2.3 0 0 1 5 1.6 2.3 2.3 0 0 1 9 5Z" fill="#7a7a7a"/></svg>457</span><span><svg width="11" height="9" viewBox="0 0 11 9"><path d="M0 0h11v6H4L1 9V6H0Z" fill="#7a7a7a"/></svg>65</span></div><div class="btn btn-sm">More</div></div></div>
</article>
<article class="abs news" style="left:141px;top:1769px">
  <div class="news-image" role="img" aria-label="Ancient stone ruins in a desert landscape" style="background:linear-gradient(180deg,#8fb0d0,#b49058 45%,#7a5a2c)"></div>
  <div class="news-body"><h3 class="news-title">The standard Lorem Ipsum passage</h3><p class="news-text">Sed ut perspiciatis unde omnis iste natus error sit voluptatem edusa accusant enim ipsam.</p>
  <div class="news-foot"><div class="stats"><span><svg width="10" height="9" viewBox="0 0 10 9"><path d="M5 9 1 5A2.3 2.3 0 0 1 5 1.6 2.3 2.3 0 0 1 9 5Z" fill="#7a7a7a"/></svg>457</span><span><svg width="11" height="9" viewBox="0 0 11 9"><path d="M0 0h11v6H4L1 9V6H0Z" fill="#7a7a7a"/></svg>65</span></div><div class="btn btn-sm">More</div></div></div>
</article>
<article class="abs news" style="left:611px;top:1769px">
  <div class="news-image" role="img" aria-label="Ornate arched palace doorway" style="background:linear-gradient(180deg,#8a8478,#5a5246)"></div>
  <div class="news-body"><h3 class="news-title">The standard Lorem Ipsum passage</h3><p class="news-text">Sed ut perspiciatis unde omnis iste natus error sit voluptatem edusa accusant enim ipsam.</p>
  <div class="news-foot"><div class="stats"><span><svg width="10" height="9" viewBox="0 0 10 9"><path d="M5 9 1 5A2.3 2.3 0 0 1 5 1.6 2.3 2.3 0 0 1 9 5Z" fill="#7a7a7a"/></svg>457</span><span><svg width="11" height="9" viewBox="0 0 11 9"><path d="M0 0h11v6H4L1 9V6H0Z" fill="#7a7a7a"/></svg>65</span></div><div class="btn btn-sm">More</div></div></div>
</article>
<article class="abs news" style="left:141px;top:1927px">
  <div class="news-image" role="img" aria-label="Carved red sandstone tower detail" style="background:linear-gradient(135deg,#a86a4e,#6a3a26)"></div>
  <div class="news-body"><h3 class="news-title">The standard Lorem Ipsum passage</h3><p class="news-text">Sed ut perspiciatis unde omnis iste natus error sit voluptatem edusa accusant enim ipsam.</p>
  <div class="news-foot"><div class="stats"><span><svg width="10" height="9" viewBox="0 0 10 9"><path d="M5 9 1 5A2.3 2.3 0 0 1 5 1.6 2.3 2.3 0 0 1 9 5Z" fill="#7a7a7a"/></svg>457</span><span><svg width="11" height="9" viewBox="0 0 11 9"><path d="M0 0h11v6H4L1 9V6H0Z" fill="#7a7a7a"/></svg>65</span></div><div class="btn btn-sm">More</div></div></div>
</article>
<article class="abs news" style="left:611px;top:1927px">
  <div class="news-image" role="img" aria-label="Avenue of stone sphinx statues" style="background:linear-gradient(135deg,#c0a080,#7e6248)"></div>
  <div class="news-body"><h3 class="news-title">The standard Lorem Ipsum passage</h3><p class="news-text">Sed ut perspiciatis unde omnis iste natus error sit voluptatem edusa accusant enim ipsam.</p>
  <div class="news-foot"><div class="stats"><span><svg width="10" height="9" viewBox="0 0 10 9"><path d="M5 9 1 5A2.3 2.3 0 0 1 5 1.6 2.3 2.3 0 0 1 9 5Z" fill="#7a7a7a"/></svg>457</span><span><svg width="11" height="9" viewBox="0 0 11 9"><path d="M0 0h11v6H4L1 9V6H0Z" fill="#7a7a7a"/></svg>65</span></div><div class="btn btn-sm">More</div></div></div>
</article>

<div class="abs btn more-news">More News</div>

<!-- footer -->
<footer class="abs footer"></footer>
<div class="abs footer-brand"><div class="brand-name">Tarn<br>Wisp</div></div>
<nav class="abs footer-nav"><span class="is-active">Home</span><span>Ancient Arts</span><span>History</span><span>News</span><span>Gallery</span><span>Articles</span><span>Contact</span></nav>
<div class="abs copyright">© 2017 TARN WISP. ALL RIGHTS RESERVED</div>
<div class="abs social" style="left:975px"></div>
<div class="abs social" style="left:1003px"></div>
<div class="abs social" style="left:1031px"></div>

</body>
</html>
```